Tidewell Homes Website Redesign

We need a website redesign for an existing website www.tidewellhomes.com.au. A home page and a property page needs to be designed...have attached layout for property page which sits under House and Land.

Have also attached logo.

Site will be built on Pyx Frame Core 5x content management system so design needs to be PFC compatible and using system fonts as well eg Arial, Verdana or Tahoma.

Target Market(s)

Builders and owner builders

Industry/Entity Type

Construction

Number of Pages Required

2 pages

Requirements
Must have
• Site Map

• o Home
• o Inclusions
• o Designs
• o House and Land
• ? Gallery
• o Selection Centre
• o Redevelopment
• o Contact Us

• Design Brief

• o Likes www.ambrosecoastal.com.au as a corporate homepage layout...with buttons across the bottom etc
• o Likes http://www.valdrenhomes.com.au/
• o Likes http://www.corvask.com.au/, but this site is built entirely in flash so some functionality won’t be possible.
• • Logo and phone number across top 02 6378 9152
• • Rolling banner along bottom of page with gallery photos
• • Horizontal navigational bar
• • Content below the main menu
• • Large contact us button.
• - Need to ensure BTG and Guild Constructor logo is on every page (perhaps in footer???)
• - Need
• ACN 061 372 908 NSW License No. 483052K ACT License No. 3142
• also in footer of every page

• Colours are, maroon, gold and predominately white. I don"t have any problems with some elements of light grey.

```html
<!DOCTYPE html>
<html lang="en">
<head>
<meta charset="utf-8">
<title>Tidewell Homes – Home Page Options</title>
<link href="https://fonts.googleapis.com/css2?family=Arimo:wght@400;700&family=Open+Sans:wght@400;700&display=swap" rel="stylesheet">
<style>
:root{
  --maroon:#8b1020;
  --maroon-deep:#5e0a14;
  --maroon-mid:#7a0d1b;
  --maroon-bright:#a3182b;
  --ink:#222;
  --text-grey:#6a6a6a;
  --rule-grey:#c8c8c8;
  --shade:#d9d9d9;
  --paper:#ffffff;
  --panel:#f4f4f4;
}
*{margin:0;padding:0;box-sizing:border-box}
html,body{width:1200px;height:2853px;overflow:hidden;background:var(--paper)}
body{position:relative;font-family:"Arimo",Arial,sans-serif;color:var(--ink)}
.option-title{position:absolute;left:0;width:1200px;text-align:center;font-size:40px;font-weight:400;letter-spacing:1px;color:#111}
.option{position:absolute;left:0;width:1200px;height:1420px}
.side-shade{position:absolute;width:18px;background:linear-gradient(90deg,#fff,#cfcfcf 55%,#eee)}
.side-shade.right{background:linear-gradient(90deg,#eee,#cfcfcf 45%,#fff)}
.brand{position:absolute;left:219px;top:160px;width:199px;height:117px;background:linear-gradient(#fff,#f3f3f3);box-shadow:0 0 6px rgba(0,0,0,.18);display:flex;align-items:center;justify-content:center;gap:8px}
.brand-dot{width:12px;height:12px;border-radius:50%;background:var(--maroon)}
.brand-name{font-size:22px;font-weight:700;color:var(--maroon)}
.call-now{position:absolute;right:209px;top:243px;font-size:19px;font-weight:700;color:var(--maroon)}
.rule{position:absolute;left:2px;width:1196px;height:3px;background:var(--maroon)}
.hero-band{position:absolute;left:2px;top:288px;width:1196px;height:295px;background:radial-gradient(ellipse at 50% 50%,var(--maroon-bright),var(--maroon-deep) 80%)}
.hero-photo{position:absolute;left:190px;top:288px;width:823px;height:295px}
.hero-photo.coastal{background:linear-gradient(180deg,#4f8fe0 0%,#b9d6f5 35%,#e9eef4 55%,#6c8cb8 75%,#5d7d3a 100%)}
.hero-photo.courtyard{background:linear-gradient(180deg,#8faa66 0%,#e6ddc9 30%,#d8cdb8 55%,#6e7a5c 78%,#4d9fc8 100%)}
.hero-quote{position:absolute;left:210px;top:514px;width:277px;height:58px;background:rgba(255,255,255,.72);padding:4px 6px;font-size:20px;line-height:24px;color:var(--maroon)}
.main-nav{position:absolute;left:207px;top:592px;height:26px;display:flex;align-items:center;list-style:none}
.main-nav li{font-size:15px;color:var(--maroon);padding:0 12px;border-left:1px solid var(--rule-grey);line-height:18px}
.main-nav li:first-child{border-left:0}
.welcome{position:absolute;left:215px;top:673px;font-size:20px;color:var(--maroon);font-weight:400}
.intro{position:absolute;left:217px;top:714px;width:482px;font-size:10.5px;line-height:15px;color:var(--text-grey)}
.intro p{margin-bottom:15px}
.intro strong{color:var(--maroon);font-weight:700}
.team-photo{float:right;width:163px;height:108px;margin:3px 0 6px 6px;border:1px solid var(--maroon);background:linear-gradient(135deg,#7a4a2e,#c9a07a 50%,#8d8f95)}
.divider{position:absolute;left:742px;top:678px;height:498px;border-left:1px dashed var(--rule-grey)}
.gallery-label{position:absolute;left:776px;top:678px;font-size:15px;color:var(--maroon)}
.gallery-main{position:absolute;left:775px;top:710px;width:214px;height:142px;border:1px solid var(--maroon);box-shadow:0 2px 4px rgba(0,0,0,.2);background:linear-gradient(180deg,#c9d3cf,#8a8f72 45%,#b0734a 70%,#a89a88)}
.thumb{position:absolute;width:106px;height:69px}
.t-warm{background:linear-gradient(135deg,#e6c48a,#c9a36a)}
.t-stair{background:linear-gradient(135deg,#b58a5a,#efe6da)}
.t-white{background:linear-gradient(135deg,#e9e9e9,#c8c3b8)}
.t-bed{background:linear-gradient(135deg,#c9a06a,#f1eadf)}
.t-lounge{background:linear-gradient(135deg,#6a3e2c,#c8b3a4)}
.t-hall{background:linear-gradient(135deg,#5a3a24,#a58f7c)}
.more{position:absolute;left:962px;top:1081px;font-family:"Open Sans",Verdana,sans-serif;font-size:9px;font-weight:700;color:#444}
.award-note{position:absolute;left:300px;top:1076px;width:300px;text-align:center;font-family:"Open Sans",Verdana,sans-serif;font-size:9.5px;line-height:11px;font-weight:700;color:#666}
.award-ribbon{position:absolute;left:229px;top:1110px;width:435px;height:82px}
.award-lines{position:absolute;left:229px;top:1120px;width:433px;text-align:center;font-size:13.5px;line-height:20px;color:#fff}
.contact-btn{position:absolute;left:789px;top:1118px;width:186px;height:72px;border-radius:8px;background:linear-gradient(180deg,var(--maroon-bright),var(--maroon-deep));box-shadow:0 3px 5px rgba(0,0,0,.35),inset 0 0 0 2px rgba(255,255,255,.25);color:#fff;font-size:20px;font-weight:700;display:flex;align-items:center;justify-content:center;letter-spacing:.5px}
.footer{position:absolute;left:0;top:1225px;width:1200px;height:144px;background:linear-gradient(180deg,var(--maroon-deep),var(--maroon-mid) 50%,var(--maroon-bright))}
.link-col{position:absolute;top:1240px;font-family:"Open Sans",Verdana,sans-serif;color:#fff}
.link-col h3{font-size:15px;font-weight:700;margin-bottom:6px;letter-spacing:.3px}
.link-col li{list-style:none;font-size:9.5px;font-weight:700;line-height:20px;letter-spacing:.5px}
.link-col li::before{content:"» ";}
.partners{position:absolute;left:769px;top:1242px;width:222px;height:114px;background:#f6f6f6;border:2px solid #ddd}
.partners-label{position:absolute;left:12px;top:7px;font-size:15px;color:var(--maroon)}
.badge-square{position:absolute;left:28px;top:36px;width:96px;height:58px;background:#dcdfe6;border-radius:2px}
.badge-round{position:absolute;left:154px;top:30px;width:56px;height:66px;border-radius:28px;background:#1d6b45}
.legal{position:absolute;left:0;top:1369px;width:1200px;height:35px;background:linear-gradient(180deg,var(--maroon-mid),var(--maroon-deep));color:#fff;text-align:center;font-family:"Open Sans",Verdana,sans-serif;font-size:9px;font-weight:700;line-height:11px;padding-top:7px}
</style>
</head>
<body>

<h2 class="option-title" style="top:48px">OPTION 1</h2>
<section class="option" style="top:0">
  <div class="side-shade" style="left:172px;top:160px;height:120px"></div>
  <div class="side-shade right" style="left:1013px;top:160px;height:120px"></div>
  <div class="brand"><span class="brand-dot"></span><span class="brand-name">Tidewell Homes</span></div>
  <div class="call-now">Call Now: 02 6378 9152</div>
  <div class="rule" style="top:283px"></div>
  <div class="hero-band"></div>
  <div class="hero-photo coastal" role="img" aria-label="Photo of a white two-storey coastal home with blue balconies"></div>
  <div class="hero-quote">“We will build your home on budget and on time”</div>
  <div class="rule" style="top:588px;height:2px"></div>
  <ul class="main-nav"><li>Home</li><li>Inclusions Designs</li><li>House and Land</li><li>Gallery</li><li>Selection Centre</li><li>Redevelopment</li><li>Contact Us</li></ul>
  <div class="rule" style="top:619px;height:2px"></div>
  <div class="side-shade" style="left:172px;top:625px;height:600px"></div>
  <div class="side-shade right" style="left:1013px;top:625px;height:600px"></div>
  <h1 class="welcome">Welcome to Tidewell Homes Constructions.</h1>
  <div class="intro">
    <div class="team-photo" role="img" aria-label="Photo of the company directors with a family"></div>
    <p><strong>Tidewell Homes Constructions</strong> was established in February 2001 by Owen Marsh and Lewis Tranter. Between the two directors the company has over 40 years building experience in the ACT Region and both directors are individually licensed builders.</p>
    <p>We offer a range of flexible and varied home designs, these designs can be built on your land or ours. We will also quote individual designs should one of our plans be unsuitable to your needs or should you desire a more customized home.</p>
    <p>Tidewell Homes is a member of the Building Trades Guild and Guild Constructors Association. In addition both directors of the company are also accredited “Ecobuild Professionals”.</p>
    <p>Tidewell Homes uses only quality suppliers and our team of contractors are reliable, qualified and assist us to achieve a quality finish.</p>
    <p>Both directors are hands on and personally oversee the construction process as well as being available to owners to attend to queries or concerns. Our aim is to build quality project homes whilst providing a boutique style service.</p>
  </div>
  <div class="divider"></div>
  <div class="gallery-label">Latest Gallery</div>
  <div class="gallery-main" role="img" aria-label="Photo of a lit modern home at dusk"></div>
  <div class="thumb t-warm" style="left:775px;top:861px" role="img" aria-label="Bathroom photo"></div>
  <div class="thumb t-stair" style="left:883px;top:861px" role="img" aria-label="Staircase photo"></div>
  <div class="thumb t-white" style="left:775px;top:933px" role="img" aria-label="Kitchen photo"></div>
  <div class="thumb t-bed" style="left:883px;top:933px" role="img" aria-label="Bedroom photo"></div>
  <div class="thumb t-lounge" style="left:775px;top:1007px" role="img" aria-label="Living room photo"></div>
  <div class="thumb t-hall" style="left:883px;top:1007px" role="img" aria-label="Hallway photo"></div>
  <div class="more">More</div>
  <div class="award-note">Award Winning Builders 02, 03 &amp; 05<br>Most Recently</div>
  <svg class="award-ribbon" viewBox="0 0 435 82" aria-hidden="true">
    <polygon points="6,4 429,4 418,41 429,78 6,78 17,41" fill="#c9c9c9"/>
    <polygon points="2,0 425,0 414,37 425,74 2,74 13,37" fill="#8b1020" stroke="#d9a3ab" stroke-width="2"/>
  </svg>
  <div class="award-lines">Winner BTG 'ACT Energy Efficient Home of the Year' 2005<br>Finalist BTG 'ACT Display Home of the Year' 2005<br>Finalist BTG 'ACT House of the Year' 2005</div>
  <div class="contact-btn">CONTACT US</div>
  <div class="footer"></div>
  <div class="link-col" style="left:217px"><h3>Links 1</h3><ul><li>Navgation 1</li><li>Navgation 2</li><li>Navgation 3</li><li>Navgation 4</li></ul></div>
  <div class="link-col" style="left:328px"><h3>Links 2</h3><ul><li>Navgation 1</li><li>Navgation 2</li><li>Navgation 3</li><li>Navgation 4</li></ul></div>
  <div class="link-col" style="left:446px"><h3>Links 3</h3><ul><li>Navgation 1</li><li>Navgation 2</li><li>Navgation 3</li><li>Navgation 4</li></ul></div>
  <div class="link-col" style="left:556px"><h3>Links 4</h3><ul><li>Navgation 1</li><li>Navgation 2</li><li>Navgation 3</li><li>Navgation 4</li></ul></div>
  <div class="partners"><span class="partners-label">Our Parners</span><span class="badge-square"></span><span class="badge-round"></span></div>
  <div class="legal">© Tidewell Homes Constructions 2004 Owned and operated by Keldor ( Canberra ) Pty Limited<br>ACN 061 372 908 NSW License No. 483052K ACT License No. 3142</div>
</section>

<h2 class="option-title" style="top:1482px">OPTION 2</h2>
<section class="option" style="top:1434px">
  <div class="side-shade" style="left:172px;top:160px;height:120px"></div>
  <div class="side-shade right" style="left:1013px;top:160px;height:120px"></div>
  <div class="brand"><span class="brand-dot"></span><span class="brand-name">Tidewell Homes</span></div>
  <div class="call-now">Call Now: 02 6378 9152</div>
  <div class="rule" style="top:283px"></div>
  <div class="hero-band"></div>
  <div class="hero-photo courtyard" role="img" aria-label="Illustration of a rendered two-storey home with pool and umbrella"></div>
  <div class="hero-quote">“We will build your home on budget and on time”</div>
  <div class="rule" style="top:588px;height:2px"></div>
  <ul class="main-nav"><li>Home</li><li>Inclusions Designs</li><li>House and Land</li><li>Gallery</li><li>Selection Centre</li><li>Redevelopment</li><li>Contact Us</li></ul>
  <div class="rule" style="top:619px;height:2px"></div>
  <div class="side-shade" style="left:172px;top:625px;height:600px"></div>
  <div class="side-shade right" style="left:1013px;top:625px;height:600px"></div>
  <h1 class="welcome">Welcome to Tidewell Homes Constructions.</h1>
  <div class="intro">
    <div class="team-photo" role="img" aria-label="Photo of the company directors with a family"></div>
    <p><strong>Tidewell Homes Constructions</strong> was established in February 2001 by Owen Marsh and Lewis Tranter. Between the two directors the company has over 40 years building experience in the ACT Region and both directors are individually licensed builders.</p>
    <p>We offer a range of flexible and varied home designs, these designs can be built on your land or ours. We will also quote individual designs should one of our plans be unsuitable to your needs or should you desire a more customized home.</p>
    <p>Tidewell Homes is a member of the Building Trades Guild and Guild Constructors Association. In addition both directors of the company are also accredited “Ecobuild Professionals”.</p>
    <p>Tidewell Homes uses only quality suppliers and our team of contractors are reliable, qualified and assist us to achieve a quality finish.</p>
    <p>Both directors are hands on and personally oversee the construction process as well as being available to owners to attend to queries or concerns. Our aim is to build quality project homes whilst providing a boutique style service.</p>
  </div>
  <div class="divider"></div>
  <div class="gallery-label">Latest Gallery</div>
  <div class="gallery-main" role="img" aria-label="Photo of a lit modern home at dusk"></div>
  <div class="thumb t-warm" style="left:775px;top:861px" role="img" aria-label="Bathroom photo"></div>
  <div class="thumb t-stair" style="left:883px;top:861px" role="img" aria-label="Staircase photo"></div>
  <div class="thumb t-white" style="left:775px;top:933px" role="img" aria-label="Kitchen photo"></div>
  <div class="thumb t-bed" style="left:883px;top:933px" role="img" aria-label="Bedroom photo"></div>
  <div class="thumb t-lounge" style="left:775px;top:1007px" role="img" aria-label="Living room photo"></div>
  <div class="thumb t-hall" style="left:883px;top:1007px" role="img" aria-label="Hallway photo"></div>
  <div class="more">More</div>
  <div class="award-note">Award Winning Builders 02, 03 &amp; 05<br>Most Recently</div>
  <svg class="award-ribbon" viewBox="0 0 435 82" aria-hidden="true">
    <polygon points="6,4 429,4 418,41 429,78 6,78 17,41" fill="#c9c9c9"/>
    <polygon points="2,0 425,0 414,37 425,74 2,74 13,37" fill="#8b1020" stroke="#d9a3ab" stroke-width="2"/>
  </svg>
  <div class="award-lines">Winner BTG 'ACT Energy Efficient Home of the Year' 2005<br>Finalist BTG 'ACT Display Home of the Year' 2005<br>Finalist BTG 'ACT House of the Year' 2005</div>
  <div class="contact-btn">CONTACT US</div>
  <div class="footer"></div>
  <div class="link-col" style="left:217px"><h3>Links 1</h3><ul><li>Navgation 1</li><li>Navgation 2</li><li>Navgation 3</li><li>Navgation 4</li></ul></div>
  <div class="link-col" style="left:328px"><h3>Links 2</h3><ul><li>Navgation 1</li><li>Navgation 2</li><li>Navgation 3</li><li>Navgation 4</li></ul></div>
  <div class="link-col" style="left:446px"><h3>Links 3</h3><ul><li>Navgation 1</li><li>Navgation 2</li><li>Navgation 3</li><li>Navgation 4</li></ul></div>
  <div class="link-col" style="left:556px"><h3>Links 4</h3><ul><li>Navgation 1</li><li>Navgation 2</li><li>Navgation 3</li><li>Navgation 4</li></ul></div>
  <div class="partners"><span class="partners-label">Our Parners</span><span class="badge-square"></span><span class="badge-round"></span></div>
  <div class="legal">© Tidewell Homes Constructions 2004 Owned and operated by Keldor ( Canberra ) Pty Limited<br>ACN 061 372 908 NSW License No. 483052K ACT License No. 3142</div>
</section>

</body>
</html>
```